Packaging Design New Cosmetics Range

Small Establish online Beauty company is expanding it's product range into Serums, Sprays and Creams . We are looking for a new fresh packaging design for this launch.
We only use products that are Organic , Not Tested on Animals and Natural products
We would be interested in viewing a White Design , Black design and a designer choice of colors .
First Products are
Rose Water in 100ml glass bottle with box
and a set of 3 Face Serums Vit C , Retinol and Hyaluronic in 30ml Glass bottle = Box
Scrubs and creams will launch later in Q1 2020 however would like a similar feel across all products
Target Market(s)
SEA / US Markets
Industry/Entity Type
Cosmetics
Colors
Designer to choose colors to be used in the design.
Requirements
Must have
- Space Allocated for Product Use and Bar Codes on Box
Nice to have
- Organic , Not tested on animal Logo's

```html
<!DOCTYPE html>
<html lang="en">
<head>
<meta charset="utf-8">
<title>Serum Labels – Vit C, Retinol &amp; Hyaluronic, Rose Water</title>
<link rel="stylesheet" href="https://fonts.googleapis.com/css2?family=Open+Sans:wght@300;400;600&family=PT+Sans+Narrow:wght@700&display=swap">
<style>
  :root {
    --bg: #e6e6e6;
    --label-black: #030303;
    --text-white: #f4f4f4;
    --text-dark: #1a1a1a;

    --vitc: #1a86d0;
    --vitc-tint: #8ccbee;
    --vitc-glow: #0a9fd8;

    --retinol: #7b6cb8;
    --retinol-tint: #b9b2de;
    --retinol-glow: #6f5fb0;

    --rose: #e0157f;
    --rose-tint: #e9a2c6;
    --rose-glow: #d8127c;
  }

  * { box-sizing: border-box; margin: 0; padding: 0; }

  html, body {
    width: 1200px;
    height: 1200px;
    overflow: hidden;
  }

  body {
    background: radial-gradient(ellipse at 50% 55%, #ffffff 0%, var(--bg) 55%, #a9a9a9 100%);
    font-family: "Open Sans", sans-serif;
    display: flex;
    align-items: center;
    justify-content: center;
  }

  .label-range {
    display: flex;
    gap: 40px;
  }

  .label {
    --accent: var(--vitc);
    --tint: var(--vitc-tint);
    --glow: var(--vitc-glow);
    position: relative;
    width: 340px;
    height: 440px;
    background: var(--label-black);
    border-top: 3px solid var(--accent);
    box-shadow: inset 0 3px 0 var(--label-black), inset 0 5px 0 var(--accent);
    display: flex;
    flex-direction: column;
    align-items: center;
    overflow: hidden;
  }

  .label--retinol { --accent: var(--retinol); --tint: var(--retinol-tint); --glow: var(--retinol-glow); }
  .label--rose    { --accent: var(--rose);    --tint: var(--rose-tint);    --glow: var(--rose-glow); }

  .brand {
    margin-top: 42px;
    display: flex;
    align-items: center;
    gap: 8px;
    color: var(--text-white);
    font-weight: 300;
    font-size: 34px;
    letter-spacing: 0.5px;
    line-height: 1;
  }

  .brand-dot {
    width: 10px;
    height: 10px;
    border-radius: 50%;
    background: var(--text-white);
  }

  .side-ornament {
    position: absolute;
    top: 78px;
    width: 70px;
    height: 120px;
    opacity: 0.55;
  }
  .side-ornament--left  { left: 0;  background: linear-gradient(90deg, var(--accent), transparent); }
  .side-ornament--right { right: 0; background: linear-gradient(270deg, var(--accent), transparent); }

  .centre-ornament {
    margin-top: 24px;
    width: 200px;
    height: 110px;
    border-radius: 50% 50% 45% 45%;
    background: radial-gradient(ellipse at 50% 60%, var(--glow) 0%, transparent 70%);
    opacity: 0.85;
  }

  .product-name {
    margin-top: 8px;
    flex: 1;
    display: flex;
    flex-direction: column;
    justify-content: center;
    text-align: center;
    color: var(--text-white);
    font-weight: 400;
    font-size: 50px;
    line-height: 1;
  }

  .product-name--split .product-line-small {
    font-size: 40px;
    margin-bottom: 4px;
  }

  .product-name--tight { font-size: 50px; }

  .band-type {
    width: 100%;
    height: 26px;
    background: var(--tint);
    color: var(--text-dark);
    font-size: 18px;
    font-weight: 400;
    text-align: center;
    line-height: 26px;
    text-transform: uppercase;
  }

  .band-volume {
    width: 100%;
    height: 42px;
    background: linear-gradient(90deg, var(--accent), color-mix(in srgb, var(--accent) 80%, white) 50%, var(--accent));
    color: var(--text-white);
    font-family: "PT Sans Narrow", sans-serif;
    font-weight: 700;
    font-size: 27px;
    text-align: center;
    line-height: 42px;
    margin-bottom: 8px;
  }
</style>
</head>
<body>
  <main class="label-range">

    <section class="label label--vitc">
      <div class="side-ornament side-ornament--left" role="img" aria-label="Blue curling leaf ornament"></div>
      <div class="side-ornament side-ornament--right" role="img" aria-label="Blue curling leaf ornament"></div>
      <div class="brand"><span class="brand-dot"></span>solvane</div>
      <div class="centre-ornament" role="img" aria-label="Soft blue floral glow"></div>
      <h2 class="product-name product-name--split">
        <span class="product-line-small">Face Serums</span>
        <span>Vit C</span>
      </h2>
      <div class="band-type">Moisturizing Serum</div>
      <div class="band-volume">1 oz / 30 ml</div>
    </section>

    <section class="label label--retinol">
      <div class="side-ornament side-ornament--left" role="img" aria-label="Violet curling leaf ornament"></div>
      <div class="side-ornament side-ornament--right" role="img" aria-label="Violet curling leaf ornament"></div>
      <div class="brand"><span class="brand-dot"></span>solvane</div>
      <div class="centre-ornament" role="img" aria-label="Soft violet floral glow"></div>
      <h2 class="product-name product-name--split">
        <span class="product-line-small">Retinol &amp;</span>
        <span class="product-line-small">Hyaluronic</span>
      </h2>
      <div class="band-type">Moisturizing Serum</div>
      <div class="band-volume">1 oz / 30 ml</div>
    </section>

    <section class="label label--rose">
      <div class="side-ornament side-ornament--left" role="img" aria-label="Pink curling leaf ornament"></div>
      <div class="side-ornament side-ornament--right" role="img" aria-label="Pink curling leaf ornament"></div>
      <div class="brand"><span class="brand-dot"></span>solvane</div>
      <div class="centre-ornament" role="img" aria-label="Soft pink floral glow"></div>
      <h2 class="product-name product-name--tight">
        <span>Rose</span>
        <span>Water</span>
      </h2>
      <div class="band-type">Moisturizing Serum</div>
      <div class="band-volume">1 oz / 30 ml</div>
    </section>

  </main>
</body>
</html>
```